Business Card Design

Our Motto is "Protecting Australia's Underground Utilities"

We want the Southern Cross inside a shield I have attached the southern cross and our old shield design

Product description is: Vacuum Excavation & Utility Location
Wet & Dry Vacuum Loading
Confined Space Entry Specialists
High Pressure Cleaning

The Southern Cross in the shield must be blue and white. The Company name must be Coastal Pipeguard Services. The Green & Gold Shield logo I uploaded is my OLD logo design. Thank you

Target Market(s)

Civil Construction

Industry/Entity Type

Business

Contact Information for Business Card

Coastal Pipeguard Services Pty Ltd
Corey Halbrook(Director)
0413862975
coreyh@pipeguardco.com.au
A.B.N.52938470116

Colors
0456a3

Requirements
Must have
• Southern Cross inside a shield, Blue and white design on the Southern Cross shield.
Must say Coastal Pipeguard Services P/L

```html
<!DOCTYPE html>
<html lang="en">
<head>
<meta charset="utf-8">
<title>Coastal Pipeguard Services – Business Card</title>
<link rel="stylesheet" href="https://fonts.googleapis.com/css2?family=Exo+2:wght@600;700&family=Open+Sans:wght@400;700&display=swap">
<style>
  :root {
    --green: #2fe000;
    --green-dark: #1f7a12;
    --blue: #2146f0;
    --ink: #111111;
    --muted: #333333;
    --paper: #ffffff;
    --backdrop: #e9e9e9;
  }
  * { box-sizing: border-box; margin: 0; padding: 0; }
  html, body { width: 1200px; height: 484px; overflow: hidden; }
  body {
    background: var(--backdrop);
    display: flex;
    align-items: center;
    justify-content: center;
    gap: 40px;
    font-family: "Open Sans", Arial, sans-serif;
  }
  .card {
    position: relative;
    width: 540px;
    height: 310px;
    background: var(--paper);
    box-shadow: 0 2px 10px rgba(0,0,0,0.18);
    overflow: hidden;
  }

  /* Front */
  .card-front .top-band {
    position: absolute; top: 0; left: 0; right: 0;
    height: 52px;
    background: var(--green);
    border-bottom: 4px solid var(--paper);
    box-shadow: 0 3px 0 var(--blue);
  }
  .card-front .abn {
    position: absolute; top: 16px; left: 290px;
    color: var(--paper);
    font-size: 13px;
    letter-spacing: 0.5px;
  }
  .brand {
    position: absolute;
    left: 40px; top: 110px;
    width: 200px;
    display: flex; flex-direction: column; align-items: center; gap: 14px;
  }
  .brand-mark {
    width: 70px; height: 70px;
    background: var(--green);
  }
  .brand-name {
    font-family: "Exo 2", Arial, sans-serif;
    font-weight: 700;
    font-size: 20px;
    line-height: 1.05;
    color: var(--green);
    text-align: center;
  }
  .contact {
    position: absolute;
    left: 280px; top: 175px;
  }
  .person-name {
    font-weight: 700; font-size: 18px; color: var(--green-dark);
  }
  .person-role {
    font-weight: 700; font-size: 17px; color: var(--blue);
    margin-bottom: 10px;
  }
  .company {
    font-family: "Exo 2", Arial, sans-serif;
    font-weight: 600; font-size: 14px; color: var(--ink);
    margin-bottom: 6px;
  }
  .line {
    display: flex; align-items: center; gap: 6px;
    font-size: 12px; color: var(--muted);
    margin-top: 3px;
  }
  .line svg { width: 12px; height: 12px; flex: none; }

  /* Back */
  .card-back {
    display: flex; flex-direction: column; align-items: center;
  }
  .card-back .brand-mark-large {
    margin-top: 60px;
    width: 130px; height: 130px;
    border-radius: 50%;
    background: var(--green);
  }
  .card-back .company-large {
    margin-top: 40px;
    font-family: "Exo 2", Arial, sans-serif;
    font-weight: 700; font-size: 22px; color: var(--ink);
  }
</style>
</head>
<body>
  <section class="card card-front">
    <div class="top-band"></div>
    <p class="abn">A.B.N.52938470116</p>

    <div class="brand">
      <div class="brand-mark"></div>
      <p class="brand-name">Coastal Pipeguard<br>Services</p>
    </div>

    <div class="contact">
      <p class="person-name">Corey Halbrook</p>
      <p class="person-role">Director</p>
      <p class="company">Coastal Pipeguard Services Pty Ltd</p>
      <p class="line">
        <svg viewBox="0 0 24 24" aria-hidden="true"><circle cx="12" cy="12" r="11" fill="none" stroke="#333" stroke-width="2"/><path d="M8 6c1 0 2 2 2 3s-1 1-1 2 2 4 3 4 1-1 2-1 3 1 3 2-1 2-2 2c-4 0-9-5-9-9 0-2 1-3 2-3z" fill="#333"/></svg>
        0413862975
      </p>
      <p class="line">
        <svg viewBox="0 0 24 24" aria-hidden="true"><circle cx="12" cy="12" r="12" fill="#333"/><path d="M5 9l7 5 7-5v8H5z" fill="#fff"/></svg>
        coreyh@pipeguardco.com.au
      </p>
    </div>
  </section>

  <section class="card card-back">
    <div class="brand-mark-large"></div>
    <p class="company-large">Coastal Pipeguard Services Pty Ltd</p>
  </section>
</body>
</html>
```